Book cover design for my new Bankruptcy Law Book

Hi

I would like to get a unique and nice design for my new book titled: "Quiet Harbors and the Lantern Keeper's Final Season".

I like blue color. It will be in Arabic so I care the most about the design of the book cover and not the words on the cover as the printing company will handle the rest.

Much appreciated,

KAREEM HADDAWI

Colors
0692cd
33a6d7
86cae7
85abd2
3277b5
0255a3

Requirements
Must have
• Blue color
Nice to have
• pictures or shapes related to bankruptcy or insolvency

```html
<!DOCTYPE html>
<html lang="en">
<head>
<meta charset="utf-8">
<title>Quiet Harbors and the Lantern Keeper's Final Season — Book Cover</title>
<link rel="stylesheet" href="https://fonts.googleapis.com/css2?family=Tajawal:wght@500;700;800&display=swap">
<style>
  :root {
    --navy: #0655a0;
    --photo-tint: #3d72ae;
    --bar: #0a3fc6;
    --bar-shade: #06339f;
    --arrow-band: #4ad0f6;
    --arrow-body: #8ff2f4;
    --arrow-edge: #3a8cf0;
    --white: #ffffff;
  }
  html, body {
    margin: 0;
    padding: 0;
    width: 800px;
    height: 1200px;
    overflow: hidden;
    background: var(--navy);
  }
  .cover {
    position: relative;
    width: 800px;
    height: 1200px;
    overflow: hidden;
    font-family: "Tajawal", sans-serif;
    color: var(--white);
  }
  .cover-art {
    position: absolute;
    inset: 0;
  }
  .cover-title {
    position: absolute;
    top: 54px;
    left: 0;
    width: 800px;
    margin: 0;
    text-align: center;
    font-size: 62px;
    font-weight: 700;
    line-height: 1;
  }
  .cover-subtitle {
    position: absolute;
    top: 194px;
    right: 40px;
    width: 420px;
    margin: 0;
    text-align: right;
    font-size: 34px;
    font-weight: 500;
    line-height: 1.6;
  }
  .cover-author {
    position: absolute;
    top: 1092px;
    left: 0;
    width: 800px;
    margin: 0;
    text-align: center;
    font-size: 30px;
    font-weight: 800;
    letter-spacing: 2px;
  }
</style>
</head>
<body>
<main class="cover">
  <svg class="cover-art" width="800" height="1200" viewBox="0 0 800 1200" xmlns="http://www.w3.org/2000/svg">
    <defs>
      <linearGradient id="photoFill" x1="0" y1="0" x2="1" y2="1">
        <stop offset="0" stop-color="#4a7fb9"/>
        <stop offset="0.5" stop-color="#3d72ae"/>
        <stop offset="1" stop-color="#4d80b8"/>
      </linearGradient>
      <linearGradient id="barFill" x1="0" y1="0" x2="1" y2="0">
        <stop offset="0" stop-color="#0a3fc6"/>
        <stop offset="1" stop-color="#0733a8"/>
      </linearGradient>
    </defs>

    <rect class="panel-navy" x="0" y="0" width="400" height="1200" fill="var(--navy)"/>

    <rect class="panel-photo" x="400" y="0" width="400" height="1200" fill="url(#photoFill)"
          role="img" aria-label="Blue-tinted photograph of banknotes"/>

    <g class="bar-chart">
      <rect x="0" y="590" width="137" height="430" rx="8" fill="url(#barFill)"/>
      <path d="M20 1020 C20 760 70 620 137 605 L137 1012 Q137 1020 129 1020 Z" fill="var(--bar-shade)" opacity="0.55"/>
      <rect x="168" y="670" width="137" height="350" rx="8" fill="url(#barFill)"/>
      <path d="M188 1020 C188 820 238 700 305 685 L305 1012 Q305 1020 297 1020 Z" fill="var(--bar-shade)" opacity="0.55"/>
      <rect x="335" y="750" width="137" height="270" rx="8" fill="url(#barFill)"/>
      <path d="M355 1020 C355 880 405 780 472 765 L472 1012 Q472 1020 464 1020 Z" fill="var(--bar-shade)" opacity="0.55"/>
    </g>

    <g class="trend-arrow">
      <polygon class="arrow-edge" points="0,285 255,380 440,802 300,806 525,1015 302,814 424,806 240,388 0,294" fill="var(--arrow-edge)"/>
      <polygon class="arrow-band" points="0,185 140,185 400,345 255,380 0,285" fill="var(--arrow-band)"/>
      <polygon class="arrow-body" points="255,380 400,345 490,802 595,785 525,1015 300,806 436,800" fill="var(--arrow-body)"/>
    </g>
  </svg>

  <h1 class="cover-title">Quiet Harbors</h1>
  <p class="cover-subtitle">and the Lantern Keeper's<br>Final Season</p>
  <p class="cover-author">KAREEM HADDAWI</p>
</main>
</body>
</html>
```